galactic arcade 80s vibes - jewelry company

I am looking for someone to build me a website for my jewelry company - I am going for an 80s retro GALACTIC arcade vibe. I want it to feel old school, be brightly colored (purples, greens, etc) encompass planets, stars, or milky way type vibes. My company is called LunoVix - it is zodiac signs & angel number jewelry. I want the website to open up as galaxy and my logo/name to pop up in the center of the screen and then go to the main page.

Industry/Entity Type

jewelry

Coding

Coded - Design and coding required

Number of Pages Required

1 page

Font styles to use
Other font styles liked:
• retro

Colors
0094D4
00A9DD
6FCCEA
C7EBF8
E9F6FB
00AB8E
00BBA5
67D7C9
C6EFE9
E9F9F6
59FF00
82FF00
B8FF75
E3FFCB
F4FFEA
FFF300
FFF600
FEFA6F
FFFEC7
FFFEE8
FFC000
F8CF3A
FAE287
FDF2CF
FEFAEE
E54698
E96AAD
F1A4CE
F9D9EA
FCEFF6
A7469A
B969AE
D3A5CF
EDDBEB
F8F0F9
6B429C
8869AF
B7A5CE
E3DAEB
F3F0F8

```html
<!DOCTYPE html>
<html lang="en">
<head>
<meta charset="utf-8">
<title>LunoVix — Zodiac &amp; Angel Number Jewelry</title>
<link rel="stylesheet" href="https://fonts.googleapis.com/css2?family=Orbitron:wght@500;700;800&family=Great+Vibes&family=Oswald:wght@400;500&family=Montserrat:wght@400;500&display=swap">
<style>
:root{
  --night:#0b0e33;
  --night-deep:#070a26;
  --violet:#3a1670;
  --violet-bright:#6b429c;
  --magenta:#e54698;
  --pink-glow:#e96aad;
  --cyan:#00a9dd;
  --cyan-soft:#6fccea;
  --green:#59ff00;
  --green-btn:#3fd60a;
  --white:#ffffff;
  --muted:#c9c6e6;
  --card-border:#6b35d6;
}
*{box-sizing:border-box;margin:0;padding:0}
html,body{width:1200px;height:5146px;overflow:hidden}
body{
  position:relative;
  background:
    radial-gradient(1px 1px at 120px 3100px,#fff8 50%,transparent 51%),
    radial-gradient(1px 1px at 930px 3650px,#fff8 50%,transparent 51%),
    radial-gradient(2px 2px at 300px 3640px,#fff6 50%,transparent 51%),
    radial-gradient(1px 1px at 1050px 2300px,#fff8 50%,transparent 51%),
    linear-gradient(180deg,var(--night) 0%,#0e1240 60%,#1a1250 82%,var(--night-deep) 100%);
  color:var(--white);
  font-family:"Montserrat",sans-serif;
}
section,header,footer{position:absolute;left:0;width:1200px}
.abs{position:absolute}
.btn{
  position:absolute;display:flex;align-items:center;justify-content:center;
  background:var(--green-btn);color:#0a2400;
  font-family:"Oswald",sans-serif;font-size:14px;font-weight:500;letter-spacing:1px;
  height:34px;border-radius:2px;
}
.script{font-family:"Great Vibes",cursive;color:var(--cyan-soft);font-size:34px;line-height:1}
.heading{font-family:"Orbitron",sans-serif;font-weight:700;font-size:26px;letter-spacing:2px;line-height:1;text-transform:uppercase}
.rule{height:4px;width:64px;background:var(--green-btn)}
.center{left:0;width:1200px;text-align:center}
.arrow{position:absolute;width:32px;height:40px}
.photo{position:absolute}

/* header */
.site-nav{top:0;height:90px}
.site-nav .link{position:absolute;top:36px;font-family:"Oswald",sans-serif;font-size:14px;letter-spacing:.5px;color:var(--white)}
.site-nav .brand{position:absolute;top:26px;left:0;width:1200px;text-align:center;font-family:"Orbitron",sans-serif;font-weight:800;font-size:30px;color:var(--green)}
.site-nav .line{position:absolute;top:70px;left:100px;width:1000px;height:1px;background:#ffffff33}

/* hero */
.hero{top:0;height:656px;background:linear-gradient(100deg,#2a0f55 0%,#571a8c 45%,#8b2fa8 70%,#4a1a80 100%)}
.hero .photo{left:660px;top:90px;width:540px;height:566px;background:radial-gradient(circle at 55% 45%,#d9a59a 0%,#8a4a8e 40%,#4b1c7a 75%,transparent 100%)}
.hero h1{position:absolute;left:98px;top:272px;font-family:"Orbitron",sans-serif;font-size:56px;letter-spacing:3px;font-weight:700;line-height:1}
.hero p{position:absolute;left:100px;top:346px;width:450px;font-size:15px;line-height:28px}

/* about */
.about{top:656px;height:564px;background:linear-gradient(180deg,#2a0b55,#3a0f6a 60%,#1a1050)}
.about .photo{left:0;top:0;width:620px;height:564px;background:radial-gradient(circle at 48% 42%,#ff3bd8 0%,#b21aa5 28%,#4b1780 60%,transparent 85%)}
.about .copy{position:absolute;left:630px;top:102px;width:470px;text-align:center}
.about p{font-size:12.5px;line-height:27.5px;color:var(--white);margin-top:26px}

/* categories */
.categories{top:1220px;height:540px}
.disc{position:absolute;border-radius:50%;box-shadow:0 0 24px #7e5cff,0 0 6px #39c4ff inset;border:3px solid #5a6cff}
.cat-label{position:absolute;width:240px;text-align:center;font-family:"Oswald",sans-serif;font-size:22px;letter-spacing:1px}

/* offer */
.offer{top:1760px;height:470px;background:linear-gradient(90deg,#141a46 0%,#151a48 50%,#2a2d66 100%)}
.offer .arcade{left:0;top:40px;width:90px;height:380px;background:linear-gradient(180deg,#3a3a10,#6b5a00,#1a1a30)}
.offer .photo.model{left:660px;top:0;width:540px;height:470px;background:radial-gradient(ellipse at 40% 40%,#b89282 0%,#5a4a6a 40%,#1f2a55 80%)}
.offer .tag{position:absolute;left:122px;top:122px;font-family:"Orbitron",sans-serif;font-weight:700;font-size:26px;letter-spacing:4px;color:var(--cyan)}
.offer .title{position:absolute;left:124px;top:170px;font-family:"Orbitron",sans-serif;font-weight:700;font-size:25px;letter-spacing:1px}
.offer .deal{position:absolute;left:124px;top:222px;font-family:"Orbitron",sans-serif;font-weight:800;font-size:36px;letter-spacing:2px;color:var(--magenta)}

/* products */
.products{top:2230px;height:650px}
.product{position:absolute;width:240px;text-align:center}
.product .name{font-family:"Oswald",sans-serif;font-size:22px;letter-spacing:.5px}
.product .sub{font-size:10px;color:var(--muted);margin-top:2px}
.product .price{font-family:"Oswald",sans-serif;font-size:24px;margin-top:8px}

/* gallery */
.gallery{top:2880px;height:720px}
.tile{position:absolute;width:318px;height:256px;background:linear-gradient(135deg,#8e96c8,#4a5590 60%,#2a3168)}

/* testimonials */
.testimonials{top:3600px;height:500px}
.quote-card{position:absolute;top:172px;width:480px;height:248px;border:3px solid var(--card-border);border-radius:4px;background:#12154a;text-align:center}
.quote-card p{margin:28px 26px 0;font-style:italic;font-size:17px;line-height:32px}
.quote-card .who{display:flex;align-items:center;justify-content:center;gap:10px;margin-top:14px}
.avatar{width:40px;height:40px;border-radius:50%;background:radial-gradient(circle,#e8c9a0,#9a7a60)}
.who .name{font-family:"Oswald",sans-serif;font-size:14px;text-align:left}
.stars{color:#ffc000;font-size:13px;letter-spacing:1px}

/* contact */
.contact{top:4100px;height:380px;background:linear-gradient(180deg,transparent,#1d1258 70%,#2a1066)}
.contact .col{position:absolute;top:70px;width:470px}
.contact .small{font-size:14px;line-height:22px}
.contact .row{display:flex;align-items:center;gap:8px;font-size:14px;margin-top:18px}
.email-input{width:468px;height:50px;background:#fff;border-radius:3px;margin-top:22px;color:#555;font-size:13px;padding:17px 26px}

/* arcade strip */
.arcades{top:4480px;height:320px;background:linear-gradient(90deg,#4a1a20 0%,#2a2e8a 30%,#1a1040 50%,#3a2aa8 70%,#6a2a9a 100%)}

/* footer */
.site-footer{top:4800px;height:346px;background:var(--night-deep)}
.site-footer .brand{position:absolute;left:100px;top:92px;font-family:"Orbitron",sans-serif;font-weight:800;font-size:28px;color:var(--green)}
.social{position:absolute;top:156px;width:36px;height:36px;border-radius:50%;border:2px solid #fff}
.fcol{position:absolute;top:74px;font-size:13px;line-height:30px}
.fcol h4{font-size:17px;font-weight:500;letter-spacing:.5px;line-height:20px;margin-bottom:8px}
.pay{position:absolute;top:176px;width:46px;height:28px;border-radius:3px;background:#e6e6ee}
.site-footer .divider{position:absolute;left:0;top:286px;width:1200px;height:1px;background:#ffffff30}
.copyright{position:absolute;top:312px;left:0;width:1200px;text-align:center;font-size:13px}
</style>
</head>
<body>

<section class="hero">
  <div class="photo" role="img" aria-label="Portrait of a model wearing gold chains and pearls against a neon ring"></div>
  <h1>LUNOVIX</h1>
  <p>Lorem ipsum dolor sit amet, consectetur adipiscing elit, sed do eiusmod tempor incididunt</p>
  <div class="btn" style="left:100px;top:418px;width:126px">SHOP NOW</div>
</section>

<header class="site-nav">
  <span class="link" style="left:108px">CATEGORIES</span>
  <span class="link" style="left:232px">ABOUT US</span>
  <span class="link" style="left:340px">CONTACT US</span>
  <span class="brand">LUNOVIX</span>
  <span class="link" style="left:758px">MY ACCOUNT</span>
  <span class="link" style="left:868px">USD &#8964;</span>
  <span class="link" style="left:940px">&#9906; SEARCH</span>
  <span class="link" style="left:1038px">&#128722;&#xFE0E; CART:0</span>
  <div class="line"></div>
</header>

<section class="about">
  <div class="photo" role="img" aria-label="Neon triangle frame with a model over a synthwave city and grid"></div>
  <div class="copy">
    <div class="script">About Us</div>
    <div class="heading" style="margin-top:4px">Welcome to LunoVix</div>
    <p>At vero eos et accusamus et iusto odio dignissimous qui blanditiis praesentium voluptatum deleniti atque corrupti quos dolores et quas molestias excepturi sint occaecati cupiditate non provident, ilique sunt in culpa qufficia deserunt mollitia animi, id est laborum et dolorum fuga. Et harum quid erum facilis est et expedita distinctio. Nam libero tempore, cum soluta nobis est eligendi optio cumque nihil impedit quo minus id quod maximeaceat facere possimus, omnis voluptas as-sumenda est, omnis dolor repellendus.</p>
  </div>
  <div class="btn" style="left:800px;top:414px;width:124px">LEARN MORE</div>
</section>

<section class="categories">
  <div class="script abs center" style="top:56px">Collections</div>
  <div class="heading abs center" style="top:92px">Shop by Category</div>
  <div class="rule abs" style="left:568px;top:130px"></div>
  <svg class="arrow" style="left:48px;top:286px" viewBox="0 0 32 40"><path d="M24 4 8 20l16 16" fill="none" stroke="#fff" stroke-width="5"/></svg>
  <svg class="arrow" style="left:1122px;top:286px" viewBox="0 0 32 40"><path d="M8 4l16 16L8 36" fill="none" stroke="#fff" stroke-width="5"/></svg>
  <div class="disc" style="left:112px;top:180px;width:188px;height:188px;background:radial-gradient(circle,#e9d9d8,#b89090)" role="img" aria-label="Necklace on a model"></div>
  <div class="disc" style="left:378px;top:180px;width:188px;height:188px;background:radial-gradient(circle,#d8d0cc,#8a7d78)" role="img" aria-label="Stacked bracelets"></div>
  <div class="disc" style="left:642px;top:180px;width:188px;height:188px;background:radial-gradient(circle,#e6dfe8,#9e98a8)" role="img" aria-label="Anklet on a foot"></div>
  <div class="disc" style="left:908px;top:180px;width:188px;height:188px;background:radial-gradient(circle,#d9a278,#8a5a3a)" role="img" aria-label="Body chain on a shoulder"></div>
  <div class="cat-label" style="left:86px;top:404px">NECKLACES</div>
  <div class="cat-label" style="left:352px;top:404px">BRACELETS</div>
  <div class="cat-label" style="left:616px;top:404px">ANKLETS</div>
  <div class="cat-label" style="left:882px;top:404px">BODY CHAINS</div>
</section>

<section class="offer">
  <div class="photo arcade" role="img" aria-label="Neon arcade cabinet"></div>
  <div class="photo model" role="img" aria-label="Model wearing drop earrings and a crystal necklace"></div>
  <div class="tag">SPECIAL OFFER</div>
  <div class="title">FINIBUS BONORUM ET</div>
  <div class="deal">UP TO 20% OFF</div>
  <div class="btn" style="left:140px;top:286px;width:124px">SHOP NOW</div>
</section>

<section class="products">
  <div class="script abs center" style="top:112px">Best Seller</div>
  <div class="heading abs center" style="top:148px">Popular Collections</div>
  <div class="rule abs" style="left:568px;top:186px"></div>
  <svg class="arrow" style="left:48px;top:310px" viewBox="0 0 32 40"><path d="M24 4 8 20l16 16" fill="none" stroke="#fff" stroke-width="5"/></svg>
  <svg class="arrow" style="left:1122px;top:310px" viewBox="0 0 32 40"><path d="M8 4l16 16L8 36" fill="none" stroke="#fff" stroke-width="5"/></svg>
  <div class="disc" style="left:112px;top:236px;width:188px;height:188px;background:radial-gradient(circle,#3a3f6a,#141a40)" role="img" aria-label="Crystal bib necklace"></div>
  <div class="disc" style="left:378px;top:236px;width:188px;height:188px;background:radial-gradient(circle,#4a3f5a,#141a40)" role="img" aria-label="Rose gold charm bracelet"></div>
  <div class="disc" style="left:642px;top:236px;width:188px;height:188px;background:radial-gradient(circle,#4a4030,#141a40)" role="img" aria-label="Gold body chain"></div>
  <div class="disc" style="left:908px;top:236px;width:188px;height:188px;background:radial-gradient(circle,#3f4358,#141a40)" role="img" aria-label="Silver chain bracelet"></div>
  <div class="product" style="left:86px;top:448px"><div class="name">FINIBUS BONORUM</div><div class="sub">Sed ut perspiciatis unde</div><div class="price">$999.00</div></div>
  <div class="product" style="left:352px;top:448px"><div class="name">FINIBUS BONORUM</div><div class="sub">Sed ut perspiciatis unde</div><div class="price">$999.00</div></div>
  <div class="product" style="left:616px;top:448px"><div class="name">FINIBUS BONORUM</div><div class="sub">Sed ut perspiciatis unde</div><div class="price">$999.00</div></div>
  <div class="product" style="left:882px;top:448px"><div class="name">FINIBUS BONORUM</div><div class="sub">Sed ut perspiciatis unde</div><div class="price">$999.00</div></div>
  <div class="btn" style="left:144px;top:556px;width:124px">SHOP NOW</div>
  <div class="btn" style="left:410px;top:556px;width:124px">SHOP NOW</div>
  <div class="btn" style="left:674px;top:556px;width:124px">SHOP NOW</div>
  <div class="btn" style="left:940px;top:556px;width:124px">SHOP NOW</div>
</section>

<section class="gallery">
  <div class="script abs center" style="top:24px">Jewelry</div>
  <div class="heading abs center" style="top:60px">Photo Gallery</div>
  <div class="rule abs" style="left:568px;top:96px"></div>
  <div class="tile" style="left:100px;top:132px" role="img" aria-label="Pendant necklace on a model"></div>
  <div class="tile" style="left:442px;top:132px" role="img" aria-label="Anklet on a bare foot"></div>
  <div class="tile" style="left:782px;top:132px" role="img" aria-label="Wide silver ring on a hand"></div>
  <div class="tile" style="left:100px;top:412px" role="img" aria-label="Stacked rings on fingers"></div>
  <div class="tile" style="left:442px;top:412px;background:linear-gradient(135deg,#c9a889,#7a5a48)" role="img" aria-label="Fine chain necklace on a neckline"></div>
  <div class="tile" style="left:782px;top:412px" role="img" aria-label="Hands wearing delicate rings"></div>
</section>

<section class="testimonials">
  <div class="script abs center" style="top:60px">Testimonial</div>
  <div class="heading abs center" style="top:96px">What Our Customer Says</div>
  <svg class="arrow" style="left:48px;top:272px" viewBox="0 0 32 40"><path d="M24 4 8 20l16 16" fill="none" stroke="#fff" stroke-width="5"/></svg>
  <svg class="arrow" style="left:1122px;top:272px" viewBox="0 0 32 40"><path d="M8 4l16 16L8 36" fill="none" stroke="#fff" stroke-width="5"/></svg>
  <div class="quote-card" style="left:100px">
    <p>&ldquo;Lorem ipsum dolor sit amet, consecteturipiscing elit, sed do eiusmod tempor incididunt ut labore et dolore magna a liqua.&rdquo;</p>
    <div class="who"><div class="avatar" role="img" aria-label="Customer portrait"></div><div><div class="name">SAM CARTER</div><div class="stars">&#9733;&#9733;&#9733;&#9733;&#9733;</div></div></div>
  </div>
  <div class="quote-card" style="left:620px">
    <p>&ldquo;Lorem ipsum dolor sit amet, consecteturipiscing elit, sed do eiusmod tempor incididunt ut labore et dolore magna a liqua.&rdquo;</p>
    <div class="who"><div class="avatar" role="img" aria-label="Customer portrait"></div><div><div class="name">SAM CARTER</div><div class="stars">&#9733;&#9733;&#9733;&#9733;&#9733;</div></div></div>
  </div>
</section>

<section class="contact">
  <div class="col" style="left:100px">
    <div class="script">Get in Touch</div>
    <div class="heading" style="margin-top:4px">Contact Details:</div>
    <div class="small" style="margin-top:28px">Need help completing your order?</div>
    <div class="row">
      <svg width="18" height="18" viewBox="0 0 24 24"><path d="M6 3l4 4-2 3c1 3 3 5 6 6l3-2 4 4-3 3C10 21 3 14 3 6z" fill="none" stroke="#fff" stroke-width="1.6"/></svg>
      <span>+1 555-014-2736</span>
      <svg width="20" height="16" viewBox="0 0 24 18" style="margin-left:10px"><rect x="1" y="1" width="22" height="16" fill="none" stroke="#fff" stroke-width="1.6"/><path d="M1 1l11 9 11-9" fill="none" stroke="#fff" stroke-width="1.6"/></svg>
      <span>info@lunovix.com</span>
    </div>
    <div class="row">
      <svg width="18" height="20" viewBox="0 0 24 28"><path d="M12 26s9-9 9-15a9 9 0 0 0-18 0c0 6 9 15 9 15z" fill="none" stroke="#fff" stroke-width="1.8"/><circle cx="12" cy="11" r="3" fill="none" stroke="#fff" stroke-width="1.8"/></svg>
      <span>48 Orbit Lane Starfall USA 30417</span>
    </div>
  </div>
  <div class="col" style="left:632px">
    <div class="script">Newsletter</div>
    <div class="heading" style="margin-top:4px">Let's Keep in Touch</div>
    <div class="small" style="margin-top:28px">Lorem ipsum dolor sit amet, consectetur adipiscing elit, sed do eiusmod tempor incidt dolore magna aliqua.</div>
    <div class="email-input">Enter Email Address</div>
  </div>
  <div class="btn" style="left:974px;top:292px;width:126px">SUBMIT NOW</div>
</section>

<section class="arcades" role="img" aria-label="Row of glowing retro arcade cabinets"></section>

<footer class="site-footer">
  <div class="brand">LUNOVIX</div>
  <div class="social" style="left:106px"></div>
  <div class="social" style="left:152px"></div>
  <div class="social" style="left:198px"></div>
  <div class="social" style="left:242px"></div>
  <div class="fcol" style="left:350px"><h4>QUICK LINKS</h4>Home<br>About<br>Proudct<br>Blog<br>Contact</div>
  <div class="fcol" style="left:520px"><h4>HELP</h4>Faq<br>Shipping &amp; returns<br>Contact us<br>Accessibility</div>
  <div class="fcol" style="left:702px"><h4>OTHERS</h4>Terms &amp; conditions<br>Privacy policy<br>Site map</div>
  <div class="fcol" style="left:888px"><h4>CONTACT</h4>+1 555-014-2736<br>info@lunovix.com</div>
  <div class="pay" style="left:888px"></div>
  <div class="pay" style="left:942px"></div>
  <div class="pay" style="left:996px"></div>
  <div class="pay" style="left:1050px"></div>
  <div class="divider"></div>
  <div class="copyright">&copy;Copyright &copy;2022 LunoVix. All Rights Reserved.</div>
</footer>

</body>
</html>
```